Packaging box design (Quorba style)

To create a striking but minimalist box for a new tool handle. The top sleeve external box dimensions are L230xW85xH65mm. We will need the logo (plim by KRV), you can use any of our rendered drawings if you feel it would look good. Information to be included; Ergonomic Adjustable Handle / 12 position lock system / Quick release shaft / Weight and space saving / Comfort grip / Ability to convert existing toolsFor purchase and converting options please visit (USA) www.halbrookinc.com or (Europe) www.krvtools.com.

Target Market(s)

Automotive professionals

Font styles to use
Sans Serif

Colors
fbed22
333333
5c5c5c
9d9d9d

Requirements
Must have
• Logo - plim by KRV (attached)

```html
<!DOCTYPE html>
<html lang="en">
<head>
<meta charset="utf-8">
<title>plim by KRV – handle box</title>
<link href="https://fonts.googleapis.com/css2?family=Roboto+Condensed:wght@400;700&family=Poppins:wght@600&display=swap" rel="stylesheet">
<style>
  :root{
    --yellow:#fbed22;
    --ink:#333333;
    --grey:#5c5c5c;
    --light-grey:#9d9d9d;
    --paper:#ffffff;
    --stage:#f1f1f1;
    --band:#2b2b2b;
  }
  *{margin:0;padding:0;box-sizing:border-box}
  html,body{width:1200px;height:794px;overflow:hidden;background:var(--stage)}
  .canvas{position:relative;width:1200px;height:794px}
  .face{position:absolute;background:var(--paper);box-shadow:0 2px 10px rgba(0,0,0,.08);overflow:hidden}
  .face--top{left:64px;top:139px;width:760px;height:281px}
  .face--side{left:64px;top:440px;width:760px;height:215px}
  .face--end{left:854px;top:440px;width:281px;height:215px}

  .brand{position:absolute;display:flex;align-items:center;gap:8px;font-family:"Poppins",sans-serif;font-weight:600;color:var(--ink);line-height:1}
  .brand__dot{width:14px;height:14px;border-radius:50%;background:var(--yellow)}
  .brand__name{font-size:28px}
  .brand__by{font-size:12px;align-self:flex-end;padding-bottom:3px}
  .face--top .brand{left:34px;top:118px}
  .face--end .brand{left:50%;top:50%;transform:translate(-50%,-50%)}
  .face--end .brand__name{font-size:38px}
  .face--end .brand__dot{width:18px;height:18px}

  .product-render{position:absolute;left:250px;top:78px;width:430px;height:124px;border-radius:62px 24px 24px 62px;
    background:linear-gradient(180deg,#f3d66a 0%,#e0b732 55%,#b98f1c 100%)}

  .features{position:absolute;left:36px;top:28px;list-style:none;font-family:"Roboto Condensed",sans-serif;font-size:15px;line-height:19px;color:var(--grey)}
  .tech-drawing{position:absolute;left:400px;top:22px;width:320px;height:120px;border-radius:10px 60px 60px 10px;
    background:linear-gradient(90deg,#f5f5f5,#e6e6e6)}
  .band{position:absolute;left:0;right:0;bottom:0;height:40px;background:var(--band);border-top:4px solid var(--yellow);
    display:flex;align-items:center;padding-left:30px;font-family:"Roboto Condensed",sans-serif;font-weight:700;font-size:14px;color:var(--paper);letter-spacing:.2px;white-space:nowrap}
</style>
</head>
<body>
<main class="canvas">
  <section class="face face--top" aria-label="Box top face">
    <div class="brand"><span class="brand__dot"></span><span class="brand__name">plim</span><span class="brand__by">by KRV</span></div>
    <div class="product-render" role="img" aria-label="Rendered yellow tool handle with black grip"></div>
  </section>
  <section class="face face--side" aria-label="Box front face">
    <ul class="features">
      <li>Ergonomic Adjustable Handle</li>
      <li>12 Position Lock System</li>
      <li>Quick Release Shaft</li>
      <li>Weight And Space Saving</li>
      <li>Comfort Grip</li>
      <li>Ability To Convert Existing Tools</li>
    </ul>
    <div class="tech-drawing" role="img" aria-label="Line drawing of the handle from above"></div>
    <div class="band">For Purchase And Converting Options Please Visit: (USA) www.halbrookinc.com or (Europe) www.krvtools.com</div>
  </section>
  <section class="face face--end" aria-label="Box end face">
    <div class="brand"><span class="brand__dot"></span><span class="brand__name">plim</span><span class="brand__by">by KRV</span></div>
  </section>
</main>
</body>
</html>
```